Tech Laundry service company looking for a new modern and clean web site

Our site is www.brightpresshub.com we are looking to rebrand our whole website.

We offer free pickup and delivery for laundry and dry cleaning in the NYC area. we target residential customers.

Sites to compare are www.fetchrinsa.com and www.zipspotless.com
Most content can be found at www.brightpresshub.com

We are looking for a clean and modern look. Nothing to busy

colors and font we use are
Logo font: Harabara
Slogan font: Swiss 721 Light Extended BT

Dark blue: C 100 M 88 Y 0 K 0
Light blue: C 85 M 50 Y 0 K 0
Orange: C 0 M 80 Y 95 K 0

Violet: C 85 M 100 Y 0 K 0

We use only Marvo, Plushe and vexbright
We are provide eco-friendly
next day laundry service

Our mission Statement is to deliver the Cleanest and Brightest clothes in the market. we use only top of the line

"We are the #1 proud supporter of Marvo and Plushe"

There will be 4 pages
the home page
and a 2 page scheduling page

THE HOME PAGE-
navigation bar must include

Home,
Clean my Clothes (schedule a pickup)
Pricing
Blog
Service Area
Commercial/Wholesale
Sign in
must have key elements about our business such as:
1. Our Price is 1.10 a lb
2. "New customers get 50% off first order and 100% off second order!"
3. we have next day service on all laundry orders
Again, you can pull the content off our current website brightpresshub.com

Order Page-

Attached please find 5 steps of the ordering page. We are looking to condense into 2
we want step2+step3+step4 on one page
then step1+step5 on the second page on step5 we want the coinrelay logo attached as well (as we do all credit card processing through CoinRelay)
at the end of the process we want to offer them to create a password to auto register
the order confirmation is attached as well. we need all that info but would like it to seem cleaner and modern.

PRICING PAGE-

Wash and Fold 1.10 per Lb ($27 min charge)
Blankets $12 and up
Bathroom Rugs $5.00 and up

Dry Cleaning
Launder and Press shirt 1.25
Suit Jacket 6.00
Pants and Skirts 6.00
2 pc suit 12.00
Dress 10.00 and up
Blouses & Sweaters 6.00

Again, we are looking for a clean and sleek site not to busy.

Based on this we will be needed another 6-8 pages of design work that will be negotiated with the winner at the end of this contest.
Good Luck!

Target Market(s)

our customers are between the ages of 22-40 years old all live in NYC

Industry/Entity Type

Dry Cleaning

Number of Pages Required

4 page

Font styles to use
Other font styles liked:
• Harabara

Requirements
Must have
• sleek and cool design
• see www.rinsa.com and zipspotless.com for concept
• Our current site is brightpresshub.com which we are looking to rebrand
Nice to have
• colors and font we use are
• Logo font: Harabara
• Slogan font: Swiss 721 Light Extended BT
• Dark blue: C 100 M 88 Y 0 K 0
• Light blue: C 85 M 50 Y 0 K 0
• Orange: C 0 M 80 Y 95 K 0
• Violet: C 85 M 100 Y 0 K 0
Should not have
• we want all the colors to be uniform. we are sending a message that we are the brightest and cleanest laundry service in the city!

```html
<!DOCTYPE html>
<html lang="en">
<head>
<meta charset="utf-8">
<title>Sudsly.com — Laundry Pickup &amp; Delivery</title>
<link href="https://fonts.googleapis.com/css2?family=Open+Sans:wght@400;600;700;800&family=Montserrat:wght@600;700;800&display=swap" rel="stylesheet">
<style>
:root{
  --dark-blue:#1e3a9a;
  --light-blue:#2a86d9;
  --orange:#ef4f22;
  --ink:#333a45;
  --muted:#7a818c;
  --line:#dfe3e8;
  --paper:#ffffff;
  --soft:#f3f5f7;
}
*{box-sizing:border-box;margin:0;padding:0}
html,body{width:1200px;height:3804px;overflow:hidden;background:var(--paper)}
body{font-family:"Open Sans",Arial,sans-serif;color:var(--ink);position:relative}
.abs{position:absolute}
h1,h2,h3,.heading{font-family:"Montserrat","Open Sans",sans-serif}

/* header */
.topline{top:14px;left:0;width:1200px;text-align:center;font-size:20px;font-weight:600;color:var(--dark-blue)}
.brand{top:66px;left:0;width:1200px;text-align:center}
.brand-name{font-family:"Open Sans",sans-serif;font-weight:700;font-size:50px;line-height:60px;color:var(--dark-blue);display:inline-flex;align-items:center;gap:14px}
.brand-name .dot{width:22px;height:22px;background:var(--light-blue);border-radius:50%}
.nav{top:168px;left:0;width:1200px;height:44px;background:#eef1f4;display:flex;justify-content:center}
.nav ul{list-style:none;display:flex}
.nav li{font-size:17px;font-weight:600;color:var(--dark-blue);padding:0 26px;line-height:44px}
.nav li.active{background:var(--light-blue);color:#fff}

/* hero */
.hero{top:212px;left:0;width:1200px;height:628px;background:linear-gradient(120deg,#c9cdd1 0%,#eef0f2 45%,#a9afb5 100%)}
.hero-offer{top:380px;left:570px;width:590px;height:300px;background:rgba(255,255,255,.88);padding:30px 36px;text-align:right}
.hero-offer .big{font-family:"Montserrat",sans-serif;font-weight:800;font-size:48px;color:var(--orange);line-height:56px}
.hero-offer .sub{font-size:24px;font-weight:600;color:var(--dark-blue);margin-top:12px;line-height:30px}
.hero-form{display:flex;justify-content:flex-end;gap:10px;margin-top:20px}
.zip{width:170px;height:54px;background:#fff;border:1px solid var(--line);font-size:20px;line-height:54px;padding-left:16px;color:var(--muted);text-align:left}
.btn-blue{height:54px;background:var(--light-blue);color:#fff;font-weight:700;font-size:22px;line-height:54px;padding:0 26px}

/* benefits */
.section-title{font-weight:800;font-size:44px;color:var(--dark-blue)}
.benefits-title{top:888px;left:120px}
.features{top:970px;left:120px;width:960px;display:flex;justify-content:space-between}
.feature{width:290px;text-align:center}
.feature svg{width:84px;height:84px}
.feature h3{font-family:"Open Sans",sans-serif;font-weight:600;font-size:20px;margin-top:14px;color:var(--ink)}
.feature p{font-size:15px;color:var(--muted);margin-top:8px;line-height:21px}
.products-title{top:1278px;left:120px;font-size:26px;font-weight:700;color:var(--dark-blue)}
.products{top:1332px;left:120px;display:flex;gap:34px;align-items:center}
.badge{width:76px;height:76px;border-radius:50%;background:#d8dde3}
.product-name{font-weight:700;font-size:30px;color:var(--dark-blue)}

/* how it works */
.steps-bg{top:1470px;left:0;width:1200px;height:480px;background:linear-gradient(180deg,#8b939b,#5b646d);clip-path:polygon(0 40px,1200px 0,1200px 480px,0 480px)}
.steps-title{top:1516px;left:0;width:1200px;text-align:center;color:#fff;font-size:46px;font-weight:800}
.step{top:1590px;width:300px;text-align:center;color:#fff}
.step .num{width:58px;height:58px;border-radius:50%;background:#fff;border:4px solid var(--orange);color:var(--orange);font-weight:800;font-size:30px;line-height:50px;margin:0 auto -14px;position:relative}
.step .circle{width:170px;height:170px;border-radius:50%;background:#fff;margin:0 auto;display:flex;align-items:center;justify-content:center}
.step h3{font-size:24px;margin-top:14px}
.step p{font-size:14px;line-height:19px;margin:6px auto 0;width:230px;opacity:.92}

/* pricing */
.pricing-title{top:1976px;left:0;width:1200px;text-align:center;font-size:40px;font-weight:800;color:var(--dark-blue)}
.pricing-offer{top:2036px;left:360px;width:480px;height:50px;border:3px solid var(--orange);text-align:center;line-height:44px;font-weight:700;font-size:21px;color:var(--dark-blue)}
.price-card{top:2116px;width:330px;height:390px;border:2px solid var(--line);background:#fff}
.price-card h3{background:var(--orange);color:#fff;font-size:24px;padding:10px 18px}
.price-card ul{list-style:none;padding:14px 18px}
.price-card li{font-size:17px;line-height:40px;border-bottom:1px solid var(--line);color:var(--muted);display:flex;align-items:center;gap:10px}
.price-card li::before{content:"";width:10px;height:10px;border-radius:50%;background:var(--orange)}
.btn-dark{position:absolute;left:18px;bottom:22px;background:var(--dark-blue);color:#fff;font-weight:600;font-size:16px;padding:10px 18px}

/* schedule banner */
.banner{top:2600px;left:0;width:1200px;height:390px;background:linear-gradient(180deg,#e9ecef,#cfd4d9)}
.banner-text{top:2690px;left:136px;color:var(--light-blue);font-weight:700;font-size:28px;line-height:36px}
.banner-text .go{font-size:44px;font-weight:800;color:var(--dark-blue);margin-top:10px;display:block}
.btn-outline{top:2850px;left:136px;border:3px solid var(--dark-blue);color:var(--dark-blue);font-weight:800;font-size:26px;padding:12px 22px;background:#fff}
.van{top:2660px;left:600px;width:500px;height:280px;border-radius:40px 120px 20px 20px;background:linear-gradient(90deg,#eef2f6,#c7d3e0)}
.arrow{top:2772px;width:40px;height:40px;border-radius:50%;background:#fff;display:flex;align-items:center;justify-content:center}

/* services */
.service{top:3030px;width:470px}
.service .ico{width:150px;height:150px;border-radius:50%;background:var(--light-blue);display:flex;align-items:center;justify-content:center;color:#fff;font-weight:800;font-size:42px;font-family:"Montserrat",sans-serif}
.service h3{font-size:24px;color:var(--dark-blue);line-height:30px}
.service p{font-size:14px;line-height:20px;color:var(--muted);margin-top:10px}

/* perks */
.perks{top:3460px;left:0;width:1200px;height:150px;background:var(--orange);clip-path:polygon(0 30px,1200px 0,1200px 110px,0 150px)}
.perk{top:3510px;display:flex;align-items:center;gap:14px;color:#fff;font-weight:700;font-size:20px;line-height:24px}

/* footer */
.socials{top:3690px;left:136px;display:flex;gap:12px}
.socials span{width:42px;height:42px;border-radius:50%;background:var(--light-blue)}
.contact{top:3660px;left:760px;font-size:16px;line-height:34px;color:var(--muted)}
.contact div{display:flex;align-items:center;gap:10px}
.copyright{top:3772px;left:0;width:1200px;text-align:center;font-size:13px;color:var(--muted)}
</style>
</head>
<body>

<header>
  <div class="abs topline">We Deliver The Cleanest &amp; Brightest Laundry In The City</div>
  <div class="abs brand">
    <div class="brand-name"><span class="dot"></span>Sudsly.com</div>
  </div>
  <nav class="abs nav">
    <ul>
      <li class="active">Home</li><li>Pricing</li><li>Clean My Clothes</li><li>About Us</li><li>Commercial / Wholesale</li><li>Help</li><li>Sign In</li>
    </ul>
  </nav>
</header>

<section>
  <div class="abs hero" role="img" aria-label="Bright laundromat with rows of front-loading washing machines"></div>
  <div class="abs hero-offer">
    <div class="big">50% off first order</div>
    <div class="big">2nd Order Free!</div>
    <div class="sub">Schedule your pickup now to have your clothes delivered by tomorrow!</div>
    <div class="hero-form"><div class="zip">Zipcode</div><div class="btn-blue">Get Clean Clothes Now</div></div>
  </div>
</section>

<section>
  <h2 class="abs section-title benefits-title">WE MAKE YOUR LIFE EASIER!</h2>
  <div class="abs features">
    <div class="feature">
      <svg viewBox="0 0 84 84"><circle cx="42" cy="26" r="14" fill="none" stroke="#2a86d9" stroke-width="5"/><path d="M14 76c2-18 14-28 28-28s26 10 28 28" fill="none" stroke="#2a86d9" stroke-width="5"/></svg>
      <h3>Trusted Professionals</h3>
      <p>Friendly professionals are experienced, trusted, background checked and insured.</p>
    </div>
    <div class="feature">
      <svg viewBox="0 0 84 84"><rect x="8" y="14" width="68" height="62" rx="6" fill="none" stroke="#2a86d9" stroke-width="5"/><path d="M8 30h68M24 6v16M60 6v16" stroke="#2a86d9" stroke-width="5"/><path d="M26 52l10 10 22-20" fill="none" stroke="#2a86d9" stroke-width="5"/></svg>
      <h3>Next-Day Availability</h3>
      <p>Book online in 60 seconds and schedule your pickup as early as tomorrow.</p>
    </div>
    <div class="feature">
      <svg viewBox="0 0 84 84"><circle cx="42" cy="42" r="34" fill="none" stroke="#2a86d9" stroke-width="5"/><path d="M28 42l10 10 20-20" fill="none" stroke="#2a86d9" stroke-width="5"/></svg>
      <h3>100% Money Back Guarantee</h3>
      <p>If you are not satisfied with our work, we'll refund your money. Its as simple as that.</p>
    </div>
  </div>
  <h3 class="abs products-title">We Only Use The Best Products</h3>
  <div class="abs products">
    <span class="badge"></span><span class="badge"></span>
    <span class="product-name">Plushe</span><span class="product-name">Marvo</span><span class="product-name">vexbright</span>
  </div>
</section>

<section>
  <div class="abs steps-bg" role="img" aria-label="Dim laundromat interior with washing machines behind the steps"></div>
  <h2 class="abs steps-title">How It Works?</h2>
  <div class="abs step" style="left:100px">
    <div class="num">1</div>
    <div class="circle"><svg width="80" height="80" viewBox="0 0 80 80"><rect x="10" y="14" width="46" height="56" fill="none" stroke="#7a818c" stroke-width="5"/><path d="M30 50l34-34 8 8-34 34H30z" fill="none" stroke="#7a818c" stroke-width="5"/></svg></div>
    <h3>Schedule</h3>
    <p>Schedule your pickup online in just a few clicks. Pick a time that suits you and we do the rest.</p>
  </div>
  <div class="abs step" style="left:450px">
    <div class="num">2</div>
    <div class="circle"><svg width="80" height="80" viewBox="0 0 80 80"><circle cx="40" cy="26" r="14" fill="none" stroke="#7a818c" stroke-width="5"/><path d="M12 72c2-16 14-26 28-26s26 10 28 26z" fill="none" stroke="#7a818c" stroke-width="5"/></svg></div>
    <h3>Pick Up</h3>
    <p>Our friendly driver will arrive at your door, collect your bag and take it to our cleaners.</p>
  </div>
  <div class="abs step" style="left:800px">
    <div class="num">3</div>
    <div class="circle"><svg width="90" height="80" viewBox="0 0 90 80"><path d="M6 20h50v40H6zM56 34h16l12 14v12H56z" fill="none" stroke="#7a818c" stroke-width="5"/><circle cx="22" cy="64" r="7" fill="#fff" stroke="#7a818c" stroke-width="5"/><circle cx="70" cy="64" r="7" fill="#fff" stroke="#7a818c" stroke-width="5"/></svg></div>
    <h3>Delivery</h3>
    <p>You'll be notified when your clothes are ready. Get them delivered fresh, clean and folded.</p>
  </div>
</section>

<section>
  <h2 class="abs pricing-title">Pricing</h2>
  <div class="abs pricing-offer">50% off first order 2nd Order Free!</div>
  <div class="abs price-card" style="left:250px">
    <h3>Wash &amp; Fold</h3>
    <ul><li>Wash and Fold $1.10</li><li>Free Marvo</li><li>Free Plushe</li><li>Free Separation</li></ul>
    <div class="btn-dark">Check out Prices</div>
  </div>
  <div class="abs price-card" style="left:620px">
    <h3>Dry Cleaning</h3>
    <ul><li>Launder and Press $1.25</li><li>Sweaters, Blouses $6.00</li><li>Blouses, Ties, Vests $4.50</li><li>Pants &amp; Skirts $7.00</li><li>Dresses &amp; Suits $10.00</li></ul>
    <div class="btn-dark">Check out Prices</div>
  </div>
</section>

<section>
  <div class="abs banner"></div>
  <div class="abs arrow" style="left:26px"><svg width="14" height="14" viewBox="0 0 14 14"><path d="M10 1L4 7l6 6" fill="none" stroke="#7a818c" stroke-width="3"/></svg></div>
  <div class="abs arrow" style="left:1134px"><svg width="14" height="14" viewBox="0 0 14 14"><path d="M4 1l6 6-6 6" fill="none" stroke="#7a818c" stroke-width="3"/></svg></div>
  <div class="abs banner-text">Schedule Your Pickup Online<br>For Next Day Delivery<span class="go">Get Started Now!</span></div>
  <div class="abs btn-outline">SCHEDULE A PICK-UP</div>
  <div class="abs van" role="img" aria-label="Branded delivery van for free pickup and delivery"></div>
</section>

<section>
  <div class="abs service" style="left:110px;display:flex;gap:22px">
    <div>
      <div class="ico"><svg width="80" height="70" viewBox="0 0 80 70"><circle cx="40" cy="20" r="12" fill="#fff"/><path d="M16 66c2-16 12-24 24-24s22 8 24 24z" fill="#fff"/><circle cx="14" cy="28" r="8" fill="#fff"/><circle cx="66" cy="28" r="8" fill="#fff"/></svg></div>
    </div>
    <div style="width:300px">
      <h3>A Customized Commercial Laundry Service</h3>
      <p>Our customer commercial laundry service is available for hotels, restaurants, gyms, salons and offices across the city. We tailor every order to your schedule and volume, with reliable pickups, clear pricing and the same bright results you trust. Contact our team to set up your account today.</p>
    </div>
  </div>
  <div class="abs service" style="left:620px;display:flex;gap:22px">
    <div><div class="ico">24/7</div></div>
    <div style="width:300px">
      <h3>Laundry Pickup and Delivery 7 Days a Week</h3>
      <p>Laundry pickup and delivery shouldn't be a hassle. That is why we accept orders online at any hour, every day of the week. Our drivers cover residential and commercial customers throughout the city, and our support team is always ready to help with any question about your order.</p>
    </div>
  </div>
</section>

<section>
  <div class="abs perks"></div>
  <div class="abs perk" style="left:210px"><svg width="44" height="44" viewBox="0 0 44 44"><circle cx="22" cy="22" r="18" fill="none" stroke="#fff" stroke-width="4"/><path d="M22 10v12l8 6" fill="none" stroke="#fff" stroke-width="4"/></svg><span>24 Hour<br>Turnaround</span></div>
  <div class="abs perk" style="left:520px"><svg width="50" height="40" viewBox="0 0 50 40"><path d="M3 8h28v22H3zM31 16h8l8 8v6H31z" fill="none" stroke="#fff" stroke-width="4"/><circle cx="12" cy="33" r="4" fill="#fff"/><circle cx="38" cy="33" r="4" fill="#fff"/></svg><span>Free Pickup<br>And Delivery</span></div>
  <div class="abs perk" style="left:860px"><svg width="44" height="44" viewBox="0 0 44 44"><rect x="4" y="6" width="36" height="26" rx="2" fill="none" stroke="#fff" stroke-width="4"/><path d="M14 40h16M22 32v8" stroke="#fff" stroke-width="4"/></svg><span>Easy Online<br>Access</span></div>
</section>

<footer>
  <div class="abs socials" aria-label="Social links"><span></span><span></span><span></span><span></span><span></span><span></span></div>
  <div class="abs contact">
    <div><svg width="18" height="22" viewBox="0 0 18 22"><path d="M9 1a8 8 0 0 0-8 8c0 6 8 12 8 12s8-6 8-12a8 8 0 0 0-8-8z" fill="#ef4f22"/><circle cx="9" cy="9" r="3" fill="#fff"/></svg>18 Harbor Lane, NY, NY 10007, USA</div>
    <div><svg width="18" height="18" viewBox="0 0 18 18"><rect x="1" y="3" width="16" height="12" fill="#ef4f22"/><path d="M1 3l8 7 8-7" fill="none" stroke="#fff" stroke-width="1.6"/></svg>contact@brightpresshub.com <span style="margin-left:24px;display:flex;align-items:center;gap:8px"><svg width="18" height="18" viewBox="0 0 18 18"><path d="M4 1l3 4-2 3c1 2 3 4 5 5l3-2 4 3-2 3C8 17 1 10 1 4z" fill="#ef4f22"/></svg>(555) 014-2290</span></div>
  </div>
  <div class="abs copyright">Copyright 2015 Sudsly.com | All Rights Reserved</div>
</footer>

</body>
</html>
```